flatrotate.co.uk landing page website design

Hi designers, I would like a custom designed landing page very similar to www.dwellingtrader.co.uk. It represents a happy place, sunny days and people swapping homes. I would like this done just like theres but our own design but a similar layout as theres.

I would like the 3 reasons to use us to be

Connect to thousands of other people in your area looking for a home swap

Our service is Completely free unlike most other exchange websites.

Find a exchange within 30 days!*

Thank you all,

Hi Everyone, I need the designs to represent london if possible like one of the designers has done for anyone else being in with a chance to win. Please check out the design by KR with the london look. I still like some of the others and they may win but i need to give this a try please.

Target Market(s)

Council house tenants

Coding

Coded - Design and coding required

Number of Pages Required

1 page

Requirements
Must have
• Custom designed landing page showing all the elements that www.dwellingtrader.co.uk use, The blue sky, and the land it shows with houses and people representing people swapping house. It can not be the same as them but can be similar concept with our own custom design and colour scheme ect.

please create 3 bubbles for speech from people. Please add the following quotes. "Its time we upsize"
"lets try and downsize and save money" "shall we move house?"
Would like 2 blocks of flats in a similar way dwelling trader.co.uk show the houses.
Nice to have

Should not have
• Same colour scheme as dwelling trader apart from the blue sky

```html
<!DOCTYPE html>
<html lang="en">
<head>
<meta charset="utf-8">
<title>flatrotate.co.uk — Swap your social home</title>
<link href="https://fonts.googleapis.com/css2?family=Mulish:wght@300;400;600;700;800;900&family=Roboto:wght@400;500;700&display=swap" rel="stylesheet">
<style>
  :root{
    --sky:#8fd3f4;
    --sky-light:#e6f5fd;
    --green:#00b035;
    --ink:#1b1b1b;
    --field:#cfcfcf;
    --footer:#1b1c1f;
    --footer-text:#9a9ca0;
    --white:#ffffff;
  }
  *{box-sizing:border-box;margin:0;padding:0}
  html,body{width:1200px;height:2249px;overflow:hidden;background:var(--white)}
  body{font-family:"Mulish",sans-serif;color:var(--ink);position:relative}

  .hero{position:absolute;left:0;top:0;width:1200px;height:1005px;background:var(--sky)}
  .brand{position:absolute;top:52px;left:0;width:1200px;display:flex;justify-content:center;align-items:center;gap:10px}
  .brand-mark{width:28px;height:28px;background:var(--green);border-radius:4px}
  .brand-name{font-weight:800;font-size:28px;color:var(--ink);letter-spacing:-.3px}
  .headline{position:absolute;top:152px;left:0;width:1200px;text-align:center;font-weight:900;font-size:46px;line-height:58px}
  .headline .accent{color:var(--green)}

  .search{position:absolute;left:86px;top:301px;width:1027px;height:136px;background:var(--sky-light);border-radius:16px}
  .search-field{position:absolute;top:24px}
  .search-field label{display:block;color:var(--green);font-weight:700;font-size:17px;margin-bottom:15px}
  .search-field .input{width:209px;height:50px;background:var(--field);border-radius:5px;font-size:18px;color:#444;padding:14px 12px;line-height:22px}
  .search-btn{position:absolute;left:858px;top:60px;width:139px;height:50px;background:var(--green);color:var(--white);border-radius:5px;font-weight:800;font-size:17px;text-align:center;line-height:50px}

  .join{position:absolute;top:470px;left:0;width:1200px;text-align:center;font-weight:900;font-size:30px;color:var(--green)}
  .join b{color:var(--ink);font-weight:900}

  .park-scene{position:absolute;left:0;top:505px;width:1200px;height:500px;
    background:linear-gradient(180deg,#dff1f7 0%,#bfd8df 18%,#7f95a8 38%,#9bb03a 62%,#7c9a12 80%,#c9cfd3 92%,#d7dbde 100%)}

  .why{position:absolute;left:0;top:1040px;width:1200px;text-align:center}
  .why h2{font-weight:900;font-size:37px;line-height:44px}
  .why h2 .accent{color:var(--green)}
  .why p{font-weight:700;font-size:19px;margin-top:6px}

  .steps{position:absolute;left:0;top:1175px;width:1200px;height:300px}
  .step-card{position:absolute;top:27px;width:234px;height:233px;border-radius:12px;display:flex;align-items:center;justify-content:center;text-align:center;color:var(--white);font-size:23px;line-height:29px;padding:0 14px}
  .step-card.green{background:var(--green)}
  .step-card.dark{background:var(--ink)}
  .step-card.bold{font-weight:800;font-size:24px;padding-bottom:14px}

  .street-scene{position:absolute;left:0;top:1523px;width:1200px;height:298px;
    background:linear-gradient(180deg,#7fd0e0 0%,#d9a07a 30%,#c98e7c 60%,#8fa9b6 85%,#cfd7dc 100%)}
  .quote{position:absolute;top:80px;width:306px;height:108px;border-radius:14px;display:flex;align-items:center;justify-content:center;text-align:center;font-size:26px;line-height:27px;color:var(--white);letter-spacing:.3px}
  .quote.dark{background:#2a2a2c}
  .quote.green{background:var(--green);font-size:20px;line-height:22px}
  .quote::before{content:"";position:absolute;inset:6px;border:2px dashed rgba(255,255,255,.85);border-radius:10px}
  .quote .tail{position:absolute;left:46px;bottom:-30px;width:0;height:0;border-right:28px solid transparent;border-top:32px solid #2a2a2c}
  .quote.green .tail{border-top-color:var(--green)}
  .quote .open,.quote .close{position:absolute;font-family:Georgia,serif;font-weight:900;font-size:56px;line-height:1;color:var(--white)}
  .quote .open{left:14px;bottom:2px}
  .quote .close{right:12px;top:6px}

  .footer{position:absolute;left:0;top:1821px;width:1200px;height:428px;background:var(--footer);color:var(--footer-text);font-family:"Roboto",sans-serif}
  .footer-brand{position:absolute;left:87px;top:60px;display:flex;align-items:center;gap:8px}
  .footer-brand .brand-mark{width:22px;height:22px;background:var(--white)}
  .footer-brand span{font-family:"Mulish",sans-serif;font-weight:800;font-size:20px;color:var(--white)}
  .footer-about{position:absolute;left:87px;top:120px;width:430px;font-size:13px;line-height:26px}
  .footer-contact{position:absolute;left:576px;top:88px;font-size:13px;line-height:21px}
  .footer-heading{color:var(--green);font-weight:700;font-size:13px;letter-spacing:3.4px}
  .footer-contact .footer-heading{margin-top:20px;margin-bottom:12px}
  .follow{margin-top:22px;padding-bottom:6px;border-bottom:1px dotted var(--footer-text);display:table}
  .footer-contact .follow{margin-bottom:0}
  .social{display:flex;gap:4px;margin-top:8px}
  .social span{width:21px;height:21px;display:block}
  .social .s1{background:#3b5998}.social .s2{background:#55acee}
  .enquiry{position:absolute;left:844px;top:56px;width:262px}
  .enquiry .footer-heading{display:flex;align-items:center;gap:14px;margin-left:9px;margin-bottom:14px}
  .enquiry .field{border:1px solid #3a3b3f;height:36px;margin-bottom:8px;font-size:13px;padding:10px 12px;color:#8a8c90}
  .enquiry .field.tall{height:66px;margin-bottom:12px}
  .submit{width:102px;height:36px;background:var(--green);color:var(--white);font-weight:700;font-size:13px;letter-spacing:3px;text-align:center;line-height:36px}
  .copyright{position:absolute;left:0;top:385px;width:1200px;text-align:center;font-family:"Mulish",sans-serif;font-weight:300;font-size:23px;color:#b3b5b8}
</style>
</head>
<body>

<header class="hero">
  <div class="brand"><span class="brand-mark"></span><span class="brand-name">flatrotate.co.uk</span></div>
  <h1 class="headline"><span class="accent">THE EASIEST WAY TO</span><br>SWAP YOUR SOCIAL HOME</h1>

  <div class="search">
    <div class="search-field" style="left:17px"><label>LOCATION</label><div class="input">TOWN</div></div>
    <div class="search-field" style="left:297px"><label>BEDROOM</label><div class="input">ANY</div></div>
    <div class="search-field" style="left:577px"><label>MAX.RENT $ PER MONTH</label><div class="input" style="margin-left:2px">ANY</div></div>
    <div class="search-btn">SEARCH</div>
  </div>

  <p class="join">JOIN <b>500,000</b> OTHER SOCIAL TENANTS ON <b>FLATROTATE</b></p>

  <div class="park-scene" role="img" aria-label="Illustration of a sunny city park with trees, tower blocks, benches and a street lamp"></div>
</header>

<section class="why">
  <h2><span class="accent">WHY CHOOSE</span> FLATROTATE?</h2>
  <p>THE UK'S LEADING MUTUAL EXCHANGE SERVICE FOR SOCIAL HOUSING</p>
</section>

<section class="steps">
  <svg width="1200" height="300" style="position:absolute;left:0;top:0" aria-hidden="true">
    <g fill="none" stroke-width="4" stroke-linecap="round">
      <path d="M113 121 V20 Q113 6 127 6 H375 Q389 6 389 20 V121" stroke="#00b035"/>
      <path d="M113 140 V268 Q113 281 127 281 H375 Q389 281 389 268 V140" stroke="#00b035" stroke-dasharray="10 10"/>
      <path d="M436 121 V20 Q436 6 450 6 H698 Q712 6 712 20 V121" stroke="#1b1b1b" stroke-dasharray="10 10"/>
      <path d="M436 140 V268 Q436 281 450 281 H698 Q712 281 712 268 V140" stroke="#1b1b1b"/>
      <path d="M764 121 V20 Q764 6 778 6 H1026 Q1040 6 1040 20 V121" stroke="#00b035"/>
      <path d="M764 140 V268 Q764 281 778 281 H1026 Q1040 281 1040 268 V140" stroke="#00b035" stroke-dasharray="10 10"/>
      <path d="M389 143 H425" stroke="#00b035"/>
      <path d="M712 143 H748" stroke="#1b1b1b"/>
      <path d="M1040 143 H1080" stroke="#00b035"/>
    </g>
    <path d="M423 133 L437 143 L423 153 Z" fill="#00b035"/>
    <path d="M746 133 L762 143 L746 153 Z" fill="#1b1b1b"/>
    <path d="M1076 133 L1090 143 L1076 153 Z" fill="#00b035"/>
  </svg>
  <div class="step-card green" style="left:133px">Connect to thou&shy;sands of other people in your area looking for a home swap</div>
  <div class="step-card dark" style="left:457px">Our service is Completely free unlike most other exchange websi&shy;tes</div>
  <div class="step-card green bold" style="left:785px">Find a<br>exchange<br>within 30 days!</div>
</section>

<section class="street-scene" role="img" aria-label="Illustration of a sunny town street with terraced shops, autumn trees and a zebra crossing">
  <div class="quote dark" style="left:86px"><span class="close">”</span>Its time we upsize<span class="open">“</span><span class="tail"></span></div>
  <div class="quote green" style="left:447px;width:310px">lets try and downsize<br>and save money<span class="close">”</span><span class="open">“</span><span class="tail"></span></div>
  <div class="quote dark" style="left:810px">shall we move<br>house?<span class="close">”</span><span class="open">“</span><span class="tail"></span></div>
</section>

<footer class="footer">
  <div class="footer-brand"><span class="brand-mark"></span><span>flatrotate.co.uk</span></div>
  <p class="footer-about">Lorem Ipsum is simply dummy text of the printing and typesetting industry. Lorem Ipsum has been the industry's standard dummy text ever since the 1500s, when an unknown printer took a galley of type and scrambled specimen book. tially unchanged. It was sheets versions of Lorem Ipsum.</p>

  <div class="footer-contact">
    <p>Your company<br>Main Road<br>City name<br>contury name</p>
    <p class="footer-heading">GENERAL ENQUIRIES</p>
    <p>+012456789<br>name@email.com</p>
    <p class="footer-heading follow">FOLLOW US</p>
    <div class="social"><span class="s1"></span><span class="s2"></span></div>
  </div>

  <form class="enquiry">
    <p class="footer-heading">
      <svg width="16" height="13" viewBox="0 0 16 13" aria-hidden="true"><rect x="1" y="2" width="14" height="10" fill="#fff"/><path d="M1 2 L8 8 L15 2" stroke="#1b1c1f" stroke-width="1.5" fill="none"/></svg>
      QUICK ENQUIRY FORM
    </p>
    <div class="field">Name</div>
    <div class="field">Email</div>
    <div class="field tall">Message</div>
    <div class="submit">SUBMIT</div>
  </form>

  <p class="copyright">flatrotate.co.uk Copyright ©&nbsp; All Rights Reserved 2020</p>
</footer>

</body>
</html>
```